Business Card for Lorena Whitfield

Name: Lorena Whitfield
Title: Realtor
Email: Lorena@LorenaWhitfieldRE.com
Phone: 480-555-0137

On the front of the business card, I would like the photo, the contact information and the Lorena Whitfield Logo. The backside is required to have the Broker logo and the required logos. Please use the colors from the logo design. Our company has a classy, professional look.

```html
<!DOCTYPE html>
<html lang="en">
<head>
<meta charset="utf-8">
<title>Lorena Whitfield – Business Card</title>
<link rel="stylesheet" href="https://fonts.googleapis.com/css2?family=Cinzel:wght@400;500&family=Libre+Caslon+Text:wght@700&family=Montserrat:wght@400;600&display=swap">
<style>
  :root {
    --backdrop: #e8263f;
    --brand-red: #c21f36;
    --deep-red: #b81f34;
    --ink: #1b1b1b;
    --paper: #ffffff;
    --photo-light: #9a9a9a;
    --photo-dark: #4a4a4a;
  }
  html, body {
    margin: 0;
    width: 1200px;
    height: 1200px;
    overflow: hidden;
    background: var(--backdrop);
  }
  .stage {
    position: relative;
    width: 1200px;
    height: 1200px;
  }
  .card {
    position: absolute;
    top: 264px;
    width: 384px;
    height: 671px;
    background: var(--paper);
  }
  .card--front { left: 162px; }
  .card--back { left: 653px; }
  .card svg { display: block; width: 100%; height: 100%; }

  .logo-name { font-family: "Cinzel", serif; font-weight: 500; fill: var(--brand-red); }
  .agent-name { font-family: "Libre Caslon Text", serif; font-weight: 700; fill: var(--ink); }
  .agent-title { font-family: "Montserrat", sans-serif; font-weight: 600; fill: var(--brand-red); }
  .contact-text { font-family: "Montserrat", sans-serif; font-weight: 400; fill: var(--ink); }
  .broker-name { font-family: "Cinzel", serif; font-weight: 400; fill: var(--ink); }
  .compliance-badge { fill: #d9d9d9; }
</style>
</head>
<body>
<main class="stage">

  <!-- Front side -->
  <section class="card card--front" aria-label="Business card front">
    <svg viewBox="0 0 618 1081" xmlns="http://www.w3.org/2000/svg">
      <defs>
        <linearGradient id="portrait-tone" x1="0" y1="0" x2="0" y2="1">
          <stop offset="0" stop-color="var(--photo-light)"/>
          <stop offset="1" stop-color="var(--photo-dark)"/>
        </linearGradient>
      </defs>

      <!-- Brand logotype -->
      <g class="brand-logo">
        <text class="logo-name" x="309" y="100" text-anchor="middle" font-size="36">LORENA WHITFIELD</text>
        <text class="logo-name" x="309" y="128" text-anchor="middle" font-size="16" letter-spacing="2">REAL ESTATE</text>
      </g>

      <!-- Black chevron bands -->
      <polygon class="band" fill="var(--ink)" points="0,250 140,330 478,330 618,250 618,590 0,590"/>
      <rect class="band-rule" x="0" y="588" width="618" height="7" fill="var(--brand-red)"/>
      <polygon class="band-accent" fill="var(--brand-red)" points="160,595 215,541 244,556 195,595"/>
      <polygon class="band-accent" fill="var(--brand-red)" points="458,595 403,541 374,556 423,595"/>
      <rect x="0" y="595" width="618" height="486" fill="var(--paper)"/>

      <!-- Portrait frame -->
      <polygon class="portrait-frame" fill="var(--paper)" stroke="var(--brand-red)" stroke-width="5"
               points="309,161 502,272 502,495 309,605 116,495 116,272"/>
      <polygon class="portrait" fill="url(#portrait-tone)" role="img" aria-label="Portrait photo of Lorena Whitfield"
               points="309,176 490,280 490,497 309,592 128,497 128,280"/>

      <!-- Name and title -->
      <text class="agent-name" x="309" y="662" text-anchor="middle" font-size="44" letter-spacing="1">Lorena Whitfield</text>
      <text class="agent-title" x="309" y="708" text-anchor="middle" font-size="30">Realtor</text>

      <!-- Email -->
      <g class="contact-icon" fill="none" stroke="var(--brand-red)" stroke-width="3">
        <polygon points="309,765 336,780 336,810 309,825 282,810 282,780"/>
        <rect x="296" y="786" width="26" height="18"/>
        <polyline points="296,786 309,798 322,786"/>
      </g>
      <text class="contact-text" x="309" y="859" text-anchor="middle" font-size="25" letter-spacing="1">Lorena@LorenaWhitfieldRE.com</text>
      <rect x="214" y="873" width="190" height="3" fill="var(--brand-red)"/>

      <!-- Phone -->
      <g class="contact-icon" fill="none" stroke="var(--brand-red)" stroke-width="3" stroke-linejoin="round">
        <polygon points="309,930 336,945 336,975 309,990 282,975 282,945"/>
        <path d="M297,950 l6,-3 l5,9 l-4,3 q3,7 10,10 l3,-4 l9,5 l-3,6 q-18,2 -26,-26 z"/>
        <path d="M312,946 l3,-6 M318,950 l5,-4 M320,957 l6,-1"/>
      </g>
      <text class="contact-text" x="309" y="1022" text-anchor="middle" font-size="25" letter-spacing="1">480-555-0137</text>
      <rect x="257" y="1036" width="104" height="3" fill="var(--brand-red)"/>
    </svg>
  </section>

  <!-- Back side -->
  <section class="card card--back" aria-label="Business card back">
    <svg viewBox="0 0 618 1081" xmlns="http://www.w3.org/2000/svg">
      <!-- Red crown band -->
      <polygon class="crown-band" fill="var(--deep-red)" points="0,0 618,0 618,362 505,430 309,323 113,430 0,362"/>

      <!-- Black side panels -->
      <polygon class="band" fill="var(--ink)" points="0,362 113,430 113,655 0,718"/>
      <polygon class="band" fill="var(--ink)" points="618,362 505,430 505,655 618,718"/>

      <!-- Broker emblem frame -->
      <polygon class="emblem-frame" fill="var(--paper)" stroke="var(--brand-red)" stroke-width="7"
               points="309,323 505,430 505,655 309,765 113,655 113,430"/>
      <polygon fill="var(--paper)" points="309,327 498,432 498,650 309,756 120,650 120,432"/>

      <!-- Broker logotype -->
      <g class="broker-logo">
        <circle cx="309" cy="515" r="60" fill="none" stroke="var(--ink)" stroke-width="6"/>
        <text class="broker-name" x="309" y="652" text-anchor="middle" font-size="30" letter-spacing="3">HARLAN CREST</text>
        <text class="broker-name" x="309" y="674" text-anchor="middle" font-size="16" letter-spacing="2">REAL ESTATE</text>
      </g>

      <!-- Compliance badge placeholders -->
      <g class="compliance-badges" role="img" aria-label="Required compliance badges">
        <rect class="compliance-badge" x="177" y="868" width="82" height="82" rx="6"/>
        <rect class="compliance-badge" x="268" y="868" width="82" height="82" rx="6"/>
        <rect class="compliance-badge" x="359" y="868" width="82" height="82" rx="6"/>
      </g>
    </svg>
  </section>

</main>
</body>
</html>
```